Tincture Design for Woman Owned CBD Branf

LumiVera is a luxery CBD brand for millennial women.

Our premium L Oil contains 500mg of full spectrum CBD derived from specially-sourced hemp for unparalleled purity and quality. Each dropper delivers approximately 20mg of CBD. Available in two flavors, Natural and Mint.

The goal is to design an aesthetically pleasing tincture (bottle dropper) with label and box. The final design should coincide with our brand guidelines and easily marketed for beauty consumers. We are looking for a clean design, the use of raised fonts and/or metallic is fine.

We have 4 other designs we'd like to work on with the winning designer.

Target Market(s)

Millennial Women, Income $75k+

Font styles to use
Other font styles liked:
• See Branding Sheet

Requirements
Must have
• Must follow brand guidelines (see attached for colors, font, etc)
Nice to have
• Raised font or Metallic Print

```html
<!DOCTYPE html>
<html lang="en">
<head>
<meta charset="utf-8">
<title>LumiVera Full Spectrum CBD Oil – Box and Label</title>
<link rel="stylesheet" href="https://fonts.googleapis.com/css2?family=Cinzel:wght@400&family=Cormorant+Garamond:wght@400&family=Montserrat:wght@400;500&display=swap">
<style>
  :root {
    --bg: #e8e4de;
    --paper: #ffffff;
    --ink: #151515;
    --brand-green: #0f5a4a;
    --gold: #c8934a;
    --malachite-dark: #06463a;
    --malachite-mid: #0d6b57;
    --malachite-light: #2a8c74;
    --frame: #1b1b1b;
  }
  * { box-sizing: border-box; margin: 0; padding: 0; }
  html, body { width: 1200px; height: 800px; overflow: hidden; }
  body {
    background: var(--bg);
    position: relative;
    font-family: "Montserrat", sans-serif;
    color: var(--ink);
  }

  .malachite {
    background:
      radial-gradient(ellipse at 30% 20%, var(--malachite-light) 0%, transparent 45%),
      radial-gradient(ellipse at 75% 70%, var(--malachite-light) 0%, transparent 40%),
      linear-gradient(160deg, var(--malachite-mid) 0%, var(--malachite-dark) 50%, var(--malachite-mid) 100%);
  }

  /* ---------- Box front panel ---------- */
  .box-front {
    position: absolute;
    left: 260px; top: 60px;
    width: 294px; height: 680px;
    background: var(--paper);
  }
  .box-front .pattern {
    position: absolute;
    left: 18px; right: 20px; top: 26px; bottom: 32px;
  }
  .box-front .label-panel {
    position: absolute;
    left: 35px; right: 36px; top: 67px; height: 399px;
    background: linear-gradient(180deg, #ffffff 0%, #ffffff 55%, #eeeeee 100%);
    border: 2px solid var(--frame);
    text-align: center;
    overflow: hidden;
  }
  .box-front .volume {
    position: absolute;
    left: 18px; right: 20px; top: 598px;
    text-align: center;
    color: #ffffff;
    font-size: 17px;
    font-weight: 400;
  }

  /* ---------- Shared label typography ---------- */
  .established {
    font-family: "Montserrat", sans-serif;
    font-size: 6px;
    letter-spacing: 3px;
    color: var(--brand-green);
  }
  .brand-name {
    font-family: "Cormorant Garamond", serif;
    font-weight: 400;
    color: var(--brand-green);
    text-transform: uppercase;
    letter-spacing: 1px;
    line-height: 1;
    white-space: nowrap;
  }
  .tagline {
    font-size: 5.5px;
    letter-spacing: 3px;
    color: var(--gold);
    text-transform: uppercase;
  }
  .spectrum {
    font-weight: 400;
    text-transform: uppercase;
    line-height: 1;
  }
  .product-name {
    font-family: "Cinzel", serif;
    font-weight: 400;
    line-height: 1;
    letter-spacing: 1px;
  }
  .strength { font-weight: 400; line-height: 1; }
  .flavor { font-weight: 400; text-transform: uppercase; line-height: 1; }

  .box-front .established { position: absolute; left: 0; right: 0; top: 30px; }
  .box-front .brand-name  { position: absolute; left: 0; right: 0; top: 84px; font-size: 34px; }
  .box-front .tagline     { position: absolute; left: 0; right: 0; top: 128px; }
  .box-front .spectrum    { position: absolute; left: 0; right: 0; top: 164px; font-size: 15px; }
  .box-front .product-name{ position: absolute; left: 0; right: 0; top: 184px; font-size: 38px; }
  .box-front .strength    { position: absolute; left: 0; right: 0; top: 256px; font-size: 24px; }
  .box-front .flavor      { position: absolute; left: 0; right: 0; top: 370px; font-size: 14px; }

  /* ---------- Bottle label (flat) ---------- */
  .bottle-label {
    position: absolute;
    left: 640px; top: 170px;
    width: 300px; height: 460px;
    background: var(--paper);
    text-align: center;
  }
  .bottle-label .band-top {
    position: absolute; left: 0; right: 0; top: 0; height: 12px;
  }
  .bottle-label .rule {
    position: absolute; left: 0; right: 0; height: 2px;
    background: var(--brand-green);
  }
  .bottle-label .rule.top { top: 16px; }
  .bottle-label .rule.bottom { top: 360px; }
  .bottle-label .band-bottom {
    position: absolute; left: 0; right: 0; top: 366px; bottom: 0;
  }
  .bottle-label .volume {
    position: absolute; left: 0; right: 0; top: 408px;
    color: #ffffff; font-size: 17px;
  }
  .bottle-label .established { position: absolute; left: 0; right: 0; top: 40px; }
  .bottle-label .brand-name  { position: absolute; left: 0; right: 0; top: 90px; font-size: 42px; }
  .bottle-label .tagline     { position: absolute; left: 0; right: 0; top: 145px; }
  .bottle-label .spectrum    { position: absolute; left: 0; right: 0; top: 180px; font-size: 17px; }
  .bottle-label .product-name{ position: absolute; left: 0; right: 0; top: 202px; font-size: 42px; }
  .bottle-label .strength    { position: absolute; left: 0; right: 0; top: 268px; font-size: 27px; }
  .bottle-label .flavor      { position: absolute; left: 0; right: 0; top: 330px; font-size: 14px; }
</style>
</head>
<body>

  <section class="box-front" aria-label="Carton front panel">
    <div class="pattern malachite" role="img" aria-label="Green malachite stone pattern"></div>
    <div class="label-panel">
      <p class="established">EST. 2020</p>
      <h1 class="brand-name">LumiVera</h1>
      <p class="tagline">Premium CBD Products</p>
      <p class="spectrum">Full Spectrum</p>
      <p class="product-name">CBD OIL</p>
      <p class="strength">500mg</p>
      <p class="flavor">Natural</p>
    </div>
    <p class="volume">1 fl oz. (30ml)</p>
  </section>

  <section class="bottle-label" aria-label="Dropper bottle label">
    <div class="band-top malachite" role="img" aria-label="Green malachite stone pattern band"></div>
    <div class="rule top"></div>
    <p class="established">EST. 2020</p>
    <h2 class="brand-name">LumiVera</h2>
    <p class="tagline">Premium CBD Products</p>
    <p class="spectrum">Full Spectrum</p>
    <p class="product-name">CBD OIL</p>
    <p class="strength">500mg</p>
    <p class="flavor">Natural</p>
    <div class="rule bottom"></div>
    <div class="band-bottom malachite" role="img" aria-label="Green malachite stone pattern band"></div>
    <p class="volume">1 fl oz. ( 30 ml )</p>
  </section>

</body>
</html>
```